Promotional Flyer/Email Design - Cabling services for Broadcast and Audio Visual

We need a promotional flyer/email design to help launch our company, Velcor Lane. We provide cabling services for Broadcast Television and Audio Visual systems. Recent projects include major television events such as the Harrowmere Racquet Classic and Audio Visual/Entertainment systems for wealthy clients in their homes and on-board super yachts.

The flyer will be printed as single sided A5 and also be sent out in the body of a promotional email. It should feature the company logo along with a complementary colour scheme. It should have a clean finish with images that show the type of work we do (cabling and equipment installation) or the setting for these systems (tv studio, super yacht, cinema room, meeting room with projector etc.)

Services we offer are:

Broadcast/AV system design
On-site installation
Rack building
Pre-fabricated cable looms
Fibre optic installation

About the company:

Velcor Lane provide cabling services for Broadcast Television and Audio Visual systems. With over 15 years experience working in these industries we can help with every aspect of design, project managment, installation and maintenance. Our projects range from fibre optic cabling at major sports events to installing and commisioning bespoke control systems on some of the worlds largest super yachts.

Contact details:

To get a quote or discuss your project contact us now
Telephone: TBC
Email: info@velcor-lane.com
Website: www.velcor-lane.com
Address: TBC

Other information:

The company is based in London, UK. Our projects often take place in other countries with work taking place accross Europe and beyond.

We have a London based workshop for rack building and cable pre-fabrication.

Our website is www.velcor-lane.com

Images:

Images attached can be editted for use on the flyer or have ideas taken from them. Only the company logo is required to feature on the final design.

Target Market(s)

Business to business

Industry/Entity Type

It Company

Font styles to use
Sans Serif

Requirements
Must have
• Company logo
• List of services
• Contact details
Nice to have
• Image of cabling, home cinema room, super yacht, luxury home, outside broadcast truck, fibre optic equipment or cabling.

```html
<!DOCTYPE html>
<html lang="en">
<head>
<meta charset="utf-8">
<title>Velcor Lane – Broadcast &amp; AV Cabling Flyer</title>
<link rel="stylesheet" href="https://fonts.googleapis.com/css2?family=Open+Sans:ital,wght@0,400;0,600;0,700;1,700&display=swap">
<style>
  :root{
    --bg:#eceaee;
    --ink:#050608;
    --blue:#1a78e2;
    --red:#e0194f;
    --orange:#f18a1c;
    --white:#ffffff;
    --grey:#c9c9c9;
    --text:#f2f2f2;
  }
  *{box-sizing:border-box;margin:0;padding:0}
  html,body{width:1041px;height:1200px;overflow:hidden;background:var(--bg)}
  body{font-family:"Open Sans",Arial,sans-serif;position:relative}
  .flyer{
    position:absolute;left:116px;top:29px;width:764px;height:1078px;
    background:var(--ink);color:var(--text);overflow:hidden;
    transform:scale(1.06);transform-origin:0 0;
    box-shadow:0 10px 30px rgba(0,0,0,.25);
  }
  .hero{position:absolute;left:0;top:0;width:764px;height:460px}
  .brand{
    position:absolute;left:54px;top:0;width:166px;height:122px;
    display:flex;align-items:center;justify-content:center;
  }
  .brand svg{position:absolute;inset:0}
  .brand-inner{position:relative;display:flex;align-items:center;gap:8px;margin-top:-10px}
  .brand-mark{width:14px;height:14px;background:var(--red)}
  .brand-name{font-weight:700;font-size:22px;color:#1d1d1d;letter-spacing:-.3px}

  .tab{
    position:absolute;left:0;height:38px;background:var(--blue);
    clip-path:polygon(0 0,calc(100% - 36px) 0,100% 100%,0 100%);
    color:var(--white);font-weight:700;font-size:27px;line-height:38px;padding-left:36px;
  }
  .tab-who{top:426px;width:230px}
  .tab-services{top:641px;width:220px}
  .tab-other{top:790px;width:333px}

  .about{position:absolute;left:30px;top:482px;width:548px;font-size:15.6px;line-height:22.5px}
  .services{position:absolute;top:698px;list-style:none;font-size:16px}
  .services li{display:flex;align-items:center;gap:14px;height:27px}
  .services-a{left:38px}
  .services-b{left:321px}
  .services-b li{height:26px}
  .tick{width:14px;height:14px;flex:none}
  .other{position:absolute;left:40px;top:846px;width:540px;font-size:15.6px;line-height:22.5px}
  .other p+p{margin-top:8px}
  .nobr{white-space:nowrap}
  .cta{
    position:absolute;left:40px;top:955px;width:463px;padding-bottom:2px;
    border-bottom:2px solid var(--blue);color:var(--blue);
    font-weight:700;font-style:italic;font-size:16px;
  }
  .contact-line{position:absolute;left:40px;top:989px;display:flex;align-items:center;gap:10px;font-size:16px;line-height:30px}
  .call-label{color:var(--orange);font-size:23px}
  .call-number{color:var(--white);font-weight:700;font-size:23px}
  .divider{width:2px;height:24px;background:var(--orange);margin:0 2px}
  .web b{color:var(--orange);font-weight:700}
  .footer{position:absolute;left:0;top:1027px;width:764px;height:51px}
  .footer-address{
    position:absolute;left:0;top:0;height:51px;width:492px;background:var(--blue);
    clip-path:polygon(0 0,100% 0,calc(100% - 22px) 100%,0 100%);
    display:flex;align-items:center;gap:8px;padding-left:40px;
    color:var(--white);font-weight:700;font-size:16px;
  }
  .footer-email{
    position:absolute;right:0;top:0;height:51px;width:288px;background:var(--orange);
    clip-path:polygon(22px 0,100% 0,100% 100%,0 100%);
    display:flex;align-items:center;gap:8px;padding-left:32px;
    color:var(--white);font-size:17px;
  }
  .footer-email b{font-weight:700}
  .work-photo{position:absolute;left:588px;width:154px;height:154px}
</style>
</head>
<body>
<main class="flyer">
  <svg class="hero" viewBox="0 0 764 460">
    <defs>
      <radialGradient id="roomTone" cx="0.55" cy="0.55" r="0.75">
        <stop offset="0" stop-color="#c9bba4"/>
        <stop offset=".35" stop-color="#a8967c"/>
        <stop offset=".7" stop-color="#6e604f"/>
        <stop offset="1" stop-color="#2f2a24"/>
      </radialGradient>
    </defs>
    <polygon role="img" aria-label="Photo of a luxury living room with wall-mounted TV, sofas and glass coffee table" points="0,0 764,0 764,300 382,388 0,300" fill="url(#roomTone)"/>
    <polygon points="0,302 382,390 764,296 764,346 382,440 0,346" fill="var(--blue)"/>
    <polyline points="0,300 382,386 764,292" fill="none" stroke="var(--grey)" stroke-width="4"/>
    <polyline points="207,344 382,384 557,344" fill="none" stroke="var(--red)" stroke-width="6"/>
    <polyline points="0,349 382,444 764,349" fill="none" stroke="var(--white)" stroke-width="5"/>
  </svg>

  <div class="brand">
    <svg viewBox="0 0 166 122" aria-hidden="true">
      <polygon points="0,0 166,0 166,102 83,122 0,102" fill="var(--blue)"/>
      <polygon points="0,0 166,0 166,96 83,116 0,96" fill="var(--white)"/>
    </svg>
    <div class="brand-inner">
      <span class="brand-mark"></span>
      <span class="brand-name">Velcor Lane</span>
    </div>
  </div>

  <h2 class="tab tab-who">Who we are</h2>
  <p class="about">Velcor Lane provide cabling services for Broadcast Television and Audio Visual systems. With over 15 years experience working in these industries we can help with every aspect of design, project managment, installation and maintenance. Our projects range from fibre optic cabling at major sports events to installing and commisioning bespoke control systems on some of the worlds largest super yachts.</p>

  <svg class="work-photo" style="top:441px" viewBox="0 0 154 154" role="img" aria-label="Photo of a cabled equipment rack">
    <defs>
      <radialGradient id="rackTone" cx="0.5" cy="0.45" r="0.6">
        <stop offset="0" stop-color="#5f7a72"/>
        <stop offset=".55" stop-color="#33403d"/>
        <stop offset="1" stop-color="#161b1a"/>
      </radialGradient>
    </defs>
    <circle cx="77" cy="77" r="66" fill="url(#rackTone)"/>
    <circle cx="77" cy="77" r="72" fill="none" stroke="var(--orange)" stroke-width="5"/>
    <path d="M77 5 A72 72 0 0 1 140 115" fill="none" stroke="var(--white)" stroke-width="5"/>
  </svg>

  <h2 class="tab tab-services">Services:</h2>
  <ul class="services services-a">
    <li><svg class="tick" viewBox="0 0 14 14"><rect x="1" y="1" width="12" height="12" fill="none" stroke="var(--blue)" stroke-width="1.6"/><path d="M3.5 7l2.5 2.5 5-6" fill="none" stroke="var(--blue)" stroke-width="1.8"/></svg>Broadcast/AV system design</li>
    <li><svg class="tick" viewBox="0 0 14 14"><rect x="1" y="1" width="12" height="12" fill="none" stroke="var(--blue)" stroke-width="1.6"/><path d="M3.5 7l2.5 2.5 5-6" fill="none" stroke="var(--blue)" stroke-width="1.8"/></svg>On-site installation</li>
    <li><svg class="tick" viewBox="0 0 14 14"><rect x="1" y="1" width="12" height="12" fill="none" stroke="var(--blue)" stroke-width="1.6"/><path d="M3.5 7l2.5 2.5 5-6" fill="none" stroke="var(--blue)" stroke-width="1.8"/></svg>Rack building</li>
  </ul>
  <ul class="services services-b">
    <li><svg class="tick" viewBox="0 0 14 14"><rect x="1" y="1" width="12" height="12" fill="none" stroke="var(--blue)" stroke-width="1.6"/><path d="M3.5 7l2.5 2.5 5-6" fill="none" stroke="var(--blue)" stroke-width="1.8"/></svg>Pre-fabricated cable looms</li>
    <li><svg class="tick" viewBox="0 0 14 14"><rect x="1" y="1" width="12" height="12" fill="none" stroke="var(--blue)" stroke-width="1.6"/><path d="M3.5 7l2.5 2.5 5-6" fill="none" stroke="var(--blue)" stroke-width="1.8"/></svg>Fibre optic installation</li>
  </ul>

  <svg class="work-photo" style="top:642px" viewBox="0 0 154 154" role="img" aria-label="Photo of a bright TV studio floor with lighting rig">
    <defs>
      <linearGradient id="studioTone" x1="0" y1="0" x2="0" y2="1">
        <stop offset="0" stop-color="#4a4f57"/>
        <stop offset=".4" stop-color="#c9ccd0"/>
        <stop offset=".65" stop-color="#eef0f2"/>
        <stop offset="1" stop-color="#8e949b"/>
      </linearGradient>
    </defs>
    <circle cx="77" cy="77" r="66" fill="url(#studioTone)"/>
    <circle cx="77" cy="77" r="72" fill="none" stroke="var(--white)" stroke-width="5"/>
    <path d="M110 13 A72 72 0 0 1 138 115" fill="none" stroke="var(--orange)" stroke-width="3"/>
  </svg>

  <h2 class="tab tab-other">Other Information</h2>
  <div class="other">
    <p>The company is based in London, UK. Our projects often take place in other countries with work taking place accross Europe and beyond.</p>
    <p>We have a London based workshop for rack building and cable <span class="nobr">pre-fabrication.</span></p>
  </div>

  <svg class="work-photo" style="top:843px" viewBox="0 0 154 154" role="img" aria-label="Photo of fibre and copper cabling on a patch frame">
    <defs>
      <linearGradient id="cableTone" x1="0" y1="0" x2="1" y2="1">
        <stop offset="0" stop-color="#d4d7da"/>
        <stop offset=".5" stop-color="#9a9ea3"/>
        <stop offset="1" stop-color="#5c6066"/>
      </linearGradient>
    </defs>
    <circle cx="77" cy="77" r="66" fill="url(#cableTone)"/>
    <circle cx="77" cy="77" r="72" fill="none" stroke="var(--red)" stroke-width="5"/>
    <path d="M77 5 A72 72 0 0 1 138 115" fill="none" stroke="var(--white)" stroke-width="4"/>
  </svg>

  <p class="cta">To get a quote or discuss your project contact us now</p>
  <div class="contact-line">
    <span class="call-label">Call Us:</span>
    <span class="call-number">5550 123 987</span>
    <span class="divider"></span>
    <svg width="18" height="18" viewBox="0 0 18 18" aria-hidden="true"><circle cx="9" cy="9" r="8" fill="none" stroke="var(--orange)" stroke-width="1.6"/><path d="M9 4a3 3 0 0 1 3 3c0 2.2-3 6-3 6s-3-3.8-3-6a3 3 0 0 1 3-3z" fill="var(--orange)"/></svg>
    <span class="web">www.<b>velcor-lane</b>.com</span>
  </div>

  <div class="footer">
    <div class="footer-address">
      <svg width="18" height="18" viewBox="0 0 18 18" aria-hidden="true"><circle cx="9" cy="9" r="8" fill="none" stroke="var(--white)" stroke-width="1.6"/><path d="M9 4a3 3 0 0 1 3 3c0 2.2-3 6-3 6s-3-3.8-3-6a3 3 0 0 1 3-3z" fill="var(--white)"/></svg>
      418 Calder Row, Eastbrook NY 10022
    </div>
    <div class="footer-email">
      <svg width="18" height="18" viewBox="0 0 18 18" aria-hidden="true"><circle cx="9" cy="9" r="8" fill="none" stroke="var(--white)" stroke-width="1.6"/><rect x="4.5" y="6" width="9" height="6.5" fill="none" stroke="var(--white)" stroke-width="1.3"/><path d="M4.5 6l4.5 3.5 4.5-3.5" fill="none" stroke="var(--white)" stroke-width="1.3"/></svg>
      <span>info@<b>velcor-lane</b>.com</span>
    </div>
  </div>
</main>
</body>
</html>
```